Tamarack Hearth Partners Business Card

Looking for a new business card layout. We are a real estate firm w/ a logo, old design attached. Must keep the same elements on there, just need a fresh look and possible some foil accents. Looking for a simpler design w/ more modern style.

Target Market(s)

Real Estate clients

Industry/Entity Type

Real Estate Agent

Contact Information for Business Card

see attached

Font styles to use
Sans Serif

Requirements
Must have
• all elements on current biz card
Nice to have
• modern look, simpler than we have!
Should not have
• no serif fonts

```html
<!DOCTYPE html>
<html lang="en">
<head>
<meta charset="utf-8">
<title>Tamarack Hearth Partners Business Card</title>
<link href="https://fonts.googleapis.com/css2?family=Montserrat:wght@400;500;700&display=swap" rel="stylesheet">
<style>
  :root {
    --backdrop: #dcdcdc;
    --card: #121212;
    --card-emboss: #1b1b1b;
    --ink: #ffffff;
    --photo-light: #e9e3d6;
    --photo-mid: #d9c3a4;
    --photo-teal: #38c9c0;
  }
  html, body {
    margin: 0;
    padding: 0;
    width: 1200px;
    height: 1200px;
    overflow: hidden;
    background: var(--backdrop);
    font-family: "Montserrat", sans-serif;
  }
  .canvas { position: relative; width: 1200px; height: 1200px; }
  .card {
    position: absolute;
    left: 168px;
    width: 893px;
    height: 511px;
    background: var(--card);
    overflow: hidden;
  }
  .card-back { top: 59px; }
  .card-front { top: 615px; }

  .emboss-name {
    position: absolute;
    left: 0; right: 0;
    top: 290px;
    text-align: center;
    font-weight: 700;
    font-size: 46px;
    letter-spacing: 1px;
    color: var(--card-emboss);
    margin: 0;
  }

  .portrait {
    position: absolute;
    left: 0; top: 0;
    width: 392px; height: 511px;
    background: linear-gradient(180deg, var(--photo-light) 0%, var(--photo-mid) 55%, var(--photo-teal) 100%);
  }
  .details {
    position: absolute;
    left: 392px; top: 0; right: 0; bottom: 0;
    color: var(--ink);
  }
  .brand-name {
    position: absolute;
    left: 12px; top: 50px;
    margin: 0;
    font-weight: 700;
    font-size: 29px;
    white-space: nowrap;
  }
  .agent {
    position: absolute;
    left: 45px; top: 140px;
  }
  .agent-name { margin: 0; font-weight: 700; font-size: 31px; line-height: 36px; }
  .agent-title { margin: 0; font-weight: 400; font-size: 23px; line-height: 30px; }
  .rule { position: absolute; left: 45px; height: 2px; background: var(--ink); }
  .rule-title { top: 214px; width: 202px; }
  .rule-address { top: 322px; width: 224px; }
  .address {
    position: absolute;
    left: 45px; top: 258px;
    margin: 0;
    font-style: normal;
    font-size: 19px;
    line-height: 31px;
    letter-spacing: 0.3px;
  }
  .contacts {
    position: absolute;
    left: 45px; top: 360px;
    margin: 0; padding: 0;
    list-style: none;
    font-size: 19px;
    letter-spacing: 0.3px;
  }
  .contacts li { display: flex; align-items: center; height: 31px; }
  .contacts svg { width: 22px; height: 22px; margin-right: 12px; flex: none; }
</style>
</head>
<body>
<div class="canvas">
  <section class="card card-back">
    <p class="emboss-name">Tamarack Hearth Partners</p>
  </section>

  <section class="card card-front">
    <div class="portrait" role="img" aria-label="Portrait photograph of the broker"></div>
    <div class="details">
      <p class="brand-name">Tamarack Hearth Partners</p>
      <div class="agent">
        <h1 class="agent-name">Marlene Voss</h1>
        <p class="agent-title">Principal Broker</p>
      </div>
      <div class="rule rule-title"></div>
      <address class="address">318 NE Juniper Way<br>Bend Falls, OR 97700</address>
      <div class="rule rule-address"></div>
      <ul class="contacts">
        <li>
          <svg viewBox="0 0 24 24" fill="#fff"><path d="M3 9c0-3 4-5 9-5s9 2 9 5l-1 2h-4l-1-2H9l-1 2H4zM6 12h12l2 7H4z"/></svg>
          555.014.2290
        </li>
        <li>
          <svg viewBox="0 0 24 24" fill="none" stroke="#fff" stroke-width="2"><rect x="7" y="2" width="10" height="20" rx="2"/><line x1="11" y1="18" x2="13" y2="18"/></svg>
          555.017.3846
        </li>
        <li>
          <svg viewBox="0 0 24 24" fill="none" stroke="#fff" stroke-width="2"><rect x="2" y="5" width="20" height="14"/><polyline points="2,5 12,13 22,5"/></svg>
          marlene@tamarackhearth.com
        </li>
        <li>
          <svg viewBox="0 0 24 24" fill="none" stroke="#fff" stroke-width="2"><circle cx="12" cy="12" r="10"/><ellipse cx="12" cy="12" rx="4" ry="10"/><line x1="2" y1="12" x2="22" y2="12"/></svg>
          tamarackhearth-homes.com
        </li>
      </ul>
    </div>
  </section>
</div>
</body>
</html>
```